Halvex Mending a Centre Pty Ltd

Business card is to promote and represent our new business. It's situated in
28 Kerro Street
Brookvale 2100 Sydney
Our clinic is all about getting people back to great health giving them back their lifestyle in half the usual time it takes to get results elsewhere , we do this through innovative therapies with latest state of the art equipment ,skills ,knowledge and experience.
We give them back their pain free healthy lifestyle with lots of energy to love life and perform their best Quickly and effectively .
The final design should communicate
Trust , confidence, results .

Reason: Waiting for some designers to submit work Thanks

Target Market(s)

High end clients that take their health and results seriously ,
High end athletes , as well as general people that want to see results with different
Treatment Methods and approach

Industry/Entity Type

Clinic

Contact Information for Business Card

Halvex Mending Centre Pty Ltd
28 Kerro Street Brookvale 2100 Sydney
Website www.halvexmendingcentre.com.au

Font styles to use
Other font styles liked:
• Gothic font medium

Requirements
Must have
• A designe that makes people look twice with a wow factor , a designe that isn't like all the rest .
• Must have the logo in the colours Iv provided in my files
• Must communicate Trust, confidence , results
Nice to have
• 1) The logo raised up or
• 2) Maybe a pop up logo on the card ?
• Or let's be creative and have two cards one on top of the other so the two cards slide .... The front will have the halvex logo with the address details etc
• The other card with have
• eg your next app .......................................repeating all way down the card
Should not have
• Basic plain looking card that everyone else has

```html
<!DOCTYPE html>
<html lang="en">
<head>
<meta charset="utf-8">
<title>Halvex Mending Centre – Business Card</title>
<link rel="stylesheet" href="https://fonts.googleapis.com/css2?family=Jost:wght@400;500;700&display=swap">
<style>
  :root {
    --stage: #e6e7ea;
    --navy: #2b2c78;
    --deep-blue: #2c2f82;
    --mid-blue: #2f6fb4;
    --light-blue: #4a9bd0;
    --green: #3d9a3a;
    --ink: #3a3a3a;
    --card-white: #fbfbfb;
    --faint: rgba(120, 120, 140, 0.10);
  }
  * { box-sizing: border-box; margin: 0; padding: 0; }
  html, body { width: 1200px; height: 900px; overflow: hidden; }
  body {
    background: var(--stage);
    font-family: "Jost", sans-serif;
    position: relative;
  }
  .card {
    position: absolute;
    left: 300px;
    width: 600px;
    height: 343px;
    border-radius: 3px;
    overflow: hidden;
    box-shadow: 0 6px 18px rgba(0,0,0,0.18);
  }

  /* Back of card */
  .card--back {
    top: 60px;
    background: linear-gradient(125deg, var(--deep-blue) 0%, var(--mid-blue) 55%, var(--light-blue) 80%, var(--mid-blue) 100%);
  }
  .card--back .glow {
    position: absolute;
    right: 40px; top: 30px;
    width: 300px; height: 280px;
    border-radius: 50%;
    background: radial-gradient(circle, rgba(120,190,230,0.35) 0%, rgba(120,190,230,0) 70%);
  }
  .back-brand {
    position: absolute;
    left: 60px;
    bottom: 70px;
    display: flex;
    align-items: center;
    gap: 14px;
    color: #f2f4f8;
    font-weight: 500;
    font-size: 34px;
    letter-spacing: 0.5px;
  }
  .brand-dot {
    width: 34px; height: 34px;
    border-radius: 50%;
    background: currentColor;
    flex: none;
  }

  /* Front of card */
  .card--front {
    top: 497px;
    background: var(--card-white);
  }
  .card--front .watermark-area {
    position: absolute;
    right: -40px; top: 40px;
    width: 320px; height: 320px;
    border-radius: 50%;
    background: radial-gradient(circle, rgba(0,0,0,0) 35%, var(--faint) 55%, rgba(0,0,0,0) 75%);
  }
  .front-brand {
    position: absolute;
    left: 44px; top: 44px;
    display: flex;
    align-items: center;
    gap: 12px;
    color: var(--navy);
    font-weight: 500;
    font-size: 32px;
  }
  .front-brand .brand-dot { width: 30px; height: 30px; color: var(--green); }

  .contacts {
    position: absolute;
    left: 44px; bottom: 40px;
    list-style: none;
    color: var(--ink);
    font-size: 15px;
    line-height: 21px;
  }
  .contacts li { display: flex; align-items: center; gap: 8px; }
  .contacts svg { width: 13px; height: 13px; fill: var(--navy); flex: none; }

  .person {
    position: absolute;
    right: 44px; top: 152px;
    text-align: right;
  }
  .person__name { color: var(--navy); font-weight: 700; font-size: 22px; line-height: 26px; }
  .person__role { color: var(--ink); font-size: 15px; line-height: 18px; }

  .address {
    position: absolute;
    right: 44px; bottom: 40px;
    text-align: right;
    color: var(--ink);
    font-size: 15px;
    line-height: 20px;
  }
  .address__company { color: var(--navy); font-weight: 700; }
</style>
</head>
<body>

  <section class="card card--back" aria-label="Card back">
    <div class="glow"></div>
    <div class="back-brand"><span class="brand-dot"></span>Halvex Mending Centre</div>
  </section>

  <section class="card card--front" aria-label="Card front">
    <div class="watermark-area" role="img" aria-label="Faint background decoration"></div>

    <div class="front-brand"><span class="brand-dot"></span>Halvex Mending Centre</div>

    <ul class="contacts">
      <li>
        <svg viewBox="0 0 24 24"><path d="M6.6 10.8a15 15 0 0 0 6.6 6.6l2.2-2.2c.3-.3.7-.4 1-.2 1.1.4 2.3.6 3.6.6.6 0 1 .4 1 1V20c0 .6-.4 1-1 1A17 17 0 0 1 3 4c0-.6.4-1 1-1h3.5c.6 0 1 .4 1 1 0 1.2.2 2.4.6 3.6.1.3 0 .7-.2 1z"/></svg>
        +61 7 5310 4472
      </li>
      <li>
        <svg viewBox="0 0 24 24"><path d="M7 1h10a2 2 0 0 1 2 2v18a2 2 0 0 1-2 2H7a2 2 0 0 1-2-2V3a2 2 0 0 1 2-2zm0 3v14h10V4zm5 15.2a1.2 1.2 0 1 0 0 2.4 1.2 1.2 0 0 0 0-2.4z"/></svg>
        0291 846 302
      </li>
      <li>
        <svg viewBox="0 0 24 24"><path d="M2 5h20v14H2zm2 2v.5l8 5 8-5V7zm0 2.8V17h16V9.8l-8 5z"/></svg>
        marcus@halvexmendingcentre.com.au
      </li>
      <li>
        <svg viewBox="0 0 24 24"><path d="M12 2a10 10 0 1 0 0 20 10 10 0 0 0 0-20zm0 2a8 8 0 0 1 6.9 4H15c-.4-1.5-1-2.8-1.7-3.9A8 8 0 0 1 12 4zM4 12c0-.7.1-1.4.3-2h3.5a16 16 0 0 0 0 4H4.3A8 8 0 0 1 4 12zm8 8a8 8 0 0 1-6.9-4H9c.5 1.9 1.5 3.4 3 4zm1.8-6h-3.6a14 14 0 0 1 0-4h3.6a14 14 0 0 1 0 4zm2.4 0a16 16 0 0 0 0-4h3.5a8 8 0 0 1 0 4z"/></svg>
        www.halvexmendingcentre.com.au
      </li>
    </ul>

    <div class="person">
      <p class="person__name">Marcus Delane</p>
      <p class="person__role">Director</p>
    </div>

    <address class="address" style="font-style: normal;">
      <span class="address__company">Halvex Mending Centre</span><br>
      Pty Ltd 28 Kerro Street Brookvale<br>
      2100 Sydney Website
    </address>
  </section>

</body>
</html>
```